Texas Civic Builders Summit Needs a Flyer

One-page event graphic/flyer and header needed. Logos provided.

2023 Texas Civic Builders Summit
Bold Ventures – True Accounts, True Answers, True Wins
August 10-11, 2023
San Antonio, Texas

About the Forum:
“Capital projects are full of risk. It’s not a question of eliminating risk, it’s a question of how to clearly identify it, reduce it, change it, or battle it.”
- Denise Holmgarten, Founder, U-BraMQ; San Antonio City Architect (retired)

Real Stories, Real Solutions, Real Success: U-BraMQ’s Texas Civic Builders Summit (TCBS) is designed to help you attain project success by hearing from Public Project Owners, architects, engineers, consultants, contractors, and suppliers. We are all in this together, and U-BraMQ is the organization that champions cross-collaboration and communication for project success!

For reference in design ONLY -
Here are some topic areas that bring project risks and/or rewards and that ultimately affect the Public Project Owner’s project success:

• Project Planning
• Regional Growth Shifts
• Project Funding
• Contracting
• Governmental Regulations
• Long-term COVID Impacts
• Infrastructure and Site Design
• Safety and Security
• Sustainability and Resilience
• Construction Predictability
• Leveraging Technology
• Facility Operations

Target Market(s)

Architects, Engineers, Contractors, project owners

Industry/Entity Type

Design and Construction

Requirements
Must have
• This is for a one-page (8.5x11) event graphic/flyer only - logos are provided. U-BraMQ logo, Texas Civic Builders Summit (TCBS) logo, 2023 Texas Civic Builders Summit, date, location
Nice to have
• Graphic(s) that represent the design and construction industry and the theme of this event (title, topics covered)
Should not have
• Full project description

```html
<!DOCTYPE html>
<html lang="en">
<head>
<meta charset="utf-8">
<title>Texas Civic Builders Summit 2023 Flyer</title>
<link href="https://fonts.googleapis.com/css2?family=Lato:wght@400;700;900&display=swap" rel="stylesheet">
<style>
  :root {
    --page-bg: #ececec;
    --paper: #ffffff;
    --navy: #1d3a8a;
    --lime: #93b52f;
    --violet-light: #8b90c6;
    --violet-dark: #2a2550;
    --ink-light: #ffffff;
  }
  html, body {
    margin: 0;
    width: 1200px;
    height: 1200px;
    overflow: hidden;
    background: var(--page-bg);
    font-family: "Lato", sans-serif;
  }
  .flyer {
    position: absolute;
    left: 288px;
    top: 158px;
    width: 623px;
    height: 884px;
    background: var(--paper);
  }
  .flyer svg { display: block; width: 100%; height: 100%; }
  .brand-name { font-family: "Lato", sans-serif; font-weight: 900; fill: var(--navy); }
  .event-kicker { font-family: "Lato", sans-serif; font-weight: 400; fill: var(--ink-light); font-size: 27px; }
  .event-title { font-family: "Lato", sans-serif; font-weight: 900; fill: var(--ink-light); font-size: 74px; }
  .event-tagline { font-family: "Lato", sans-serif; font-weight: 700; fill: var(--ink-light); font-size: 29px; }
  .event-detail { font-family: "Lato", sans-serif; font-weight: 700; fill: var(--ink-light); font-size: 37px; }
  .partner-name { font-family: "Lato", sans-serif; font-weight: 400; fill: #4a4a4a; font-size: 46px; }
</style>
</head>
<body>
<div class="flyer">
  <svg viewBox="0 0 1003 1424" xmlns="http://www.w3.org/2000/svg">
    <defs>
      <linearGradient id="cityTones" x1="0" y1="0" x2="0" y2="1">
        <stop offset="0" stop-color="#5e5388"/>
        <stop offset="0.25" stop-color="#8f6f99"/>
        <stop offset="0.34" stop-color="#d59a7e"/>
        <stop offset="0.45" stop-color="#4a3a55"/>
        <stop offset="0.75" stop-color="#8a5a3a"/>
        <stop offset="1" stop-color="#3b2c30"/>
      </linearGradient>
      <linearGradient id="bandTones" x1="0" y1="0" x2="1" y2="1">
        <stop offset="0" stop-color="var(--violet-light)"/>
        <stop offset="0.6" stop-color="#4d4a80"/>
        <stop offset="1" stop-color="var(--violet-dark)"/>
      </linearGradient>
      <clipPath id="paperClip"><rect width="1003" height="1424"/></clipPath>
    </defs>

    <g clip-path="url(#paperClip)">
      <!-- city skyline photo area -->
      <ellipse class="city-photo" role="img" aria-label="Aerial photo of a downtown skyline at dusk with lit towers and highways"
               cx="560" cy="630" rx="575" ry="430" fill="url(#cityTones)"/>

      <!-- violet info band -->
      <path class="info-band" d="M0 746 C 180 960 420 1062 700 1062 C 820 1062 900 1050 925 1036 C 760 1230 600 1340 440 1424 L0 1424 Z" fill="url(#bandTones)"/>

      <!-- green swooshes -->
      <path class="swoosh-top" d="M88 436 C 300 150 700 60 1003 215 L1003 270 C 700 150 330 200 88 436 Z" fill="var(--lime)"/>
      <path class="swoosh-left" d="M0 426 C 30 720 220 930 470 998 C 230 960 40 800 0 660 Z" fill="var(--lime)"/>
    </g>

    <!-- summit name -->
    <text class="brand-name" x="60" y="120" font-size="40">Texas Civic</text>
    <text class="brand-name" x="60" y="168" font-size="40">Builders Summit</text>

    <!-- event copy -->
    <text class="event-kicker" x="55" y="1028">2023 Texas</text>
    <text class="event-kicker" x="55" y="1064">Civic Builders Summit</text>
    <text class="event-title" x="53" y="1148">BOLD VENTURES</text>
    <text class="event-tagline" x="53" y="1202">True Accounts, True Answers, True Wins</text>

    <!-- calendar icon -->
    <g class="icon-calendar" fill="none" stroke="#fff" stroke-width="3">
      <rect x="58" y="1242" width="38" height="36" rx="4"/>
      <line x1="58" y1="1254" x2="96" y2="1254"/>
      <line x1="68" y1="1237" x2="68" y2="1247"/>
      <line x1="86" y1="1237" x2="86" y2="1247"/>
      <circle cx="90" cy="1274" r="8" fill="var(--violet-light)"/>
    </g>
    <text class="event-detail" x="55" y="1325">10-11 th</text>
    <text class="event-detail" x="55" y="1368">Aug,2023</text>

    <line class="detail-divider" x1="246" y1="1238" x2="246" y2="1378" stroke="#fff" stroke-width="3"/>

    <!-- pin icon -->
    <g class="icon-pin" fill="none" stroke="#fff" stroke-width="3">
      <path d="M310 1278 C 296 1262 292 1254 292 1248 A 18 18 0 0 1 328 1248 C 328 1254 324 1262 310 1278 Z"/>
      <circle cx="310" cy="1248" r="6"/>
    </g>
    <text class="event-detail" x="293" y="1325">San Antonio,</text>
    <text class="event-detail" x="293" y="1368">Texas</text>

    <!-- partner organisation -->
    <circle class="partner-dot" cx="848" cy="1250" r="44" fill="var(--navy)"/>
    <text class="partner-name" x="848" y="1350" text-anchor="middle">U-BraMQ</text>
  </svg>
</div>
</body>
</html>
```